High end building company who specialise in architecturally designed homes needing a presentation do

We need a document/template that can be used in Indesign. We present proposal's, house plans, specifications at various stages throughout a building project from initial contact right through to completion. We want to have the same feel through out each presentation and be able to use the same first few pages and then be able to insert the contents. Sometimes the content will be A4 and other times when presenting plans will be A3. I have attached an example of one previously used for presenting plans (see 01_Conceptual) and one for proposals (see Proposal Example ). The document needs to have a minimalist look and feel very sophisticated to suit our client base. The look of the document should tie in with our logo design which is also attached.

```html
<!DOCTYPE html>
<html lang="en">
<head>
<meta charset="utf-8">
<title>Kalvenhoek — Vandermolen Residence Presentation Pages</title>
<link href="https://fonts.googleapis.com/css2?family=Kumbh+Sans:wght@500;700;800&family=Lato:wght@300;400;700&display=swap" rel="stylesheet">
<style>
  :root{
    --board:#231f20;
    --ink:#000000;
    --paper:#ffffff;
    --mist:#c9c9c9;
    --stone-light:#e6e2dc;
    --stone-dark:#b9b3aa;
    --map-grey:#a9aaa8;
    --foliage:#3f5a33;
    --label:#6d6d6d;
    --numeral:#a7a7a7;
    --ghost:#141414;
    --leather:#8a6a3a;
    --corridor:#4a3d32;
    --render:#c7ccd0;
    --lot-edge:#2fb7c9;
  }
  *{margin:0;padding:0;box-sizing:border-box}
  html,body{width:1199px;height:1200px;overflow:hidden;background:var(--board)}
  .board{position:relative;width:1199px;height:1200px;background:var(--board)}
  .page{position:absolute;width:499px;height:351px;background:var(--paper);overflow:hidden}
  .page svg{display:block;width:100%;height:100%}
  .page--cover{left:91px;top:51px}
  .page--contents{left:610px;top:51px}
  .page--brief{left:91px;top:421px}
  .page--section{left:610px;top:421px}
  .page--site-area{left:91px;top:797px}
  .page--site-lot{left:610px;top:797px}
  .display{font-family:"Kumbh Sans",sans-serif;font-weight:800;fill:var(--ink)}
  .wordmark{font-family:"Kumbh Sans",sans-serif;font-weight:800;fill:var(--ink);letter-spacing:-1px}
  .band-caption{font-family:"Lato",sans-serif;font-weight:700;fill:var(--paper)}
  .heading{font-family:"Kumbh Sans",sans-serif;font-weight:700;fill:var(--ink)}
  .index-label{font-family:"Lato",sans-serif;font-weight:400;fill:var(--label)}
  .numeral{font-family:"Lato",sans-serif;font-weight:400;fill:var(--numeral)}
  .ghost-numeral{font-family:"Lato",sans-serif;font-weight:400;fill:var(--ghost)}
  .brief-title{font-family:"Lato",sans-serif;font-weight:700;fill:var(--ink)}
  .brief-text{font-family:"Lato",sans-serif;font-weight:400;fill:#222}
  .guide{stroke:#8a8a8a;stroke-width:1;stroke-dasharray:4 3;fill:none}
</style>
</head>
<body>
<div class="board">
  <svg width="0" height="0" style="position:absolute">
    <defs>
      <linearGradient id="sheen" x1="0" x2="1" y1="0" y2="0">
        <stop offset="0" stop-color="#bdbdbd"/>
        <stop offset="0.35" stop-color="#ffffff"/>
      </linearGradient>
      <linearGradient id="sheen-right" x1="0" x2="1">
        <stop offset="0.6" stop-color="#ffffff"/>
        <stop offset="1" stop-color="#c4c4c4"/>
      </linearGradient>
      <linearGradient id="stone" x1="0" x2="1" y1="0" y2="1">
        <stop offset="0" stop-color="var(--stone-light)"/>
        <stop offset="0.5" stop-color="var(--stone-dark)"/>
        <stop offset="1" stop-color="var(--stone-light)"/>
      </linearGradient>
    </defs>
  </svg>

  <!-- Cover -->
  <section class="page page--cover">
    <svg viewBox="0 0 623 439" preserveAspectRatio="none">
      <rect x="0" y="330" width="623" height="109" fill="url(#sheen)"/>
      <polygon points="0,112 160,112 215,330 0,330" fill="var(--ink)"/>
      <text class="ghost-numeral" x="8" y="318" font-size="170">01</text>
      <polygon points="165,143 623,143 623,330 215,330" fill="url(#stone)" role="img" aria-label="Close-up photograph of pale layered stone texture"/>
      <polygon points="212,330 595,330 595,360 220,360" fill="var(--ink)"/>
      <text class="band-caption" x="592" y="350" font-size="11" text-anchor="end">Vandermolen Residence Concept Design</text>
      <line class="guide" x1="133" y1="0" x2="237" y2="439"/>
      <text class="wordmark" x="598" y="114" font-size="58" text-anchor="end">kalvenhoek</text>
    </svg>
  </section>

  <!-- Contents -->
  <section class="page page--contents">
    <svg viewBox="0 0 623 439" preserveAspectRatio="none">
      <rect x="0" y="0" width="623" height="439" fill="url(#sheen-right)"/>
      <line class="guide" x1="75" y1="0" x2="108" y2="130"/>
      <line class="guide" x1="215" y1="0" x2="245" y2="130"/>
      <line class="guide" x1="355" y1="0" x2="385" y2="130"/>
      <line class="guide" x1="150" y1="350" x2="170" y2="439"/>
      <line class="guide" x1="290" y1="350" x2="310" y2="439"/>
      <line class="guide" x1="435" y1="352" x2="455" y2="439"/>
      <text class="heading" x="33" y="67" font-size="19">Vandermolen Residence</text>
      <text class="heading" x="33" y="94" font-size="19">Contents</text>
      <polygon points="0,120 108,120 150,340 0,340" fill="var(--leather)" role="img" aria-label="Photograph of a leather notebook cover on a desk"/>
      <polygon points="108,134 245,134 285,350 150,350" fill="#8f938c" role="img" aria-label="Aerial photograph of the site"/>
      <circle cx="198" cy="228" r="72" fill="var(--foliage)" role="img" aria-label="Circular aerial view of the neighbourhood"/>
      <polygon points="245,120 385,120 430,345 285,345" fill="var(--corridor)" role="img" aria-label="Photograph of a lit timber stair corridor"/>
      <polygon points="385,134 550,134 580,352 435,352" fill="var(--render)" stroke="#555" stroke-width="1.5" role="img" aria-label="Concept render of the residence and driveway"/>
      <text class="index-label" x="20" y="372" font-size="12">00</text>
      <text class="index-label" x="20" y="388" font-size="12">Outline Brief</text>
      <text class="index-label" x="175" y="372" font-size="12">01</text>
      <text class="index-label" x="175" y="388" font-size="12">Project Details</text>
      <text class="index-label" x="316" y="355" font-size="12">02</text>
      <text class="index-label" x="316" y="371" font-size="12">Visual</text>
      <text class="index-label" x="316" y="387" font-size="12">Benchmarking</text>
      <text class="index-label" x="456" y="372" font-size="12">03</text>
      <text class="index-label" x="456" y="388" font-size="12">Concept Design</text>
    </svg>
  </section>

  <!-- Outline brief -->
  <section class="page page--brief">
    <svg viewBox="0 0 623 439" preserveAspectRatio="none">
      <rect x="0" y="0" width="623" height="439" fill="url(#sheen)"/>
      <text class="numeral" x="24" y="93" font-size="64">00</text>
      <g class="brief">
        <text class="brief-title" x="197" y="47" font-size="14">Vandermolen Residence</text>
        <text class="brief-title" x="197" y="67" font-size="14">Outline Brief</text>
        <text class="brief-text" font-size="11">
          <tspan x="197" y="91">Location</tspan>
          <tspan x="197" y="105">148 Harbour Road</tspan>
          <tspan x="197" y="119">Eastvale</tspan>
          <tspan x="197" y="133">QLD 4190</tspan>
          <tspan x="197" y="161">Site Area</tspan>
          <tspan x="197" y="175">10,120m²</tspan>
        </text>
        <text class="brief-text" font-size="9">
          <tspan x="197" y="210">Client Requirements</tspan>
          <tspan x="197" y="222">Bedrooms</tspan>
          <tspan x="197" y="235">Bathrooms</tspan>
          <tspan x="197" y="247">Living Areas</tspan>
          <tspan x="197" y="260">Outdoor Living Area</tspan>
          <tspan x="197" y="272">Kitchen</tspan>
          <tspan x="197" y="285">Study</tspan>
          <tspan x="197" y="297">Laundry</tspan>
          <tspan x="197" y="310">Powder Room</tspan>
          <tspan x="197" y="322">Storage</tspan>
          <tspan x="197" y="335">Double Garage</tspan>
          <tspan x="197" y="366">Special Requirements</tspan>
          <tspan x="197" y="379">Small walk-in wardrobes and study desk to children's rooms</tspan>
          <tspan x="197" y="391">Existing Pool to remain</tspan>
          <tspan x="197" y="404">Existing Jacaranda tree to remain</tspan>
        </text>
        <text class="brief-text" font-size="9">
          <tspan x="332" y="222">4</tspan>
          <tspan x="332" y="235">2</tspan>
          <tspan x="332" y="247">2</tspan>
        </text>
      </g>
    </svg>
  </section>

  <!-- Section divider -->
  <section class="page page--section">
    <svg viewBox="0 0 623 439" preserveAspectRatio="none">
      <rect x="0" y="0" width="623" height="439" fill="url(#sheen)"/>
      <polygon points="0,112 160,112 215,330 0,330" fill="var(--ink)"/>
      <text class="ghost-numeral" x="8" y="318" font-size="170">01</text>
      <polygon points="168,143 623,143 623,330 215,330" fill="url(#stone)" role="img" aria-label="Close-up photograph of pale layered stone texture"/>
      <polygon points="212,330 623,330 623,360 220,360" fill="var(--ink)"/>
      <line class="guide" x1="133" y1="0" x2="237" y2="439"/>
      <text class="display" x="588" y="82" font-size="36" text-anchor="end">01</text>
      <text class="display" x="588" y="120" font-size="36" text-anchor="end">Project Details</text>
    </svg>
  </section>

  <!-- Site location: area -->
  <section class="page page--site-area">
    <svg viewBox="0 0 623 439" preserveAspectRatio="none">
      <rect x="0" y="0" width="623" height="439" fill="url(#sheen)"/>
      <polygon points="0,112 45,112 100,330 0,330" fill="var(--ink)"/>
      <polygon points="55,143 623,143 623,330 100,330" fill="var(--map-grey)" role="img" aria-label="Greyed aerial map of the surrounding suburb"/>
      <circle cx="348" cy="242" r="85" fill="var(--foliage)" role="img" aria-label="Circular aerial view of the neighbourhood around the site"/>
      <polygon points="100,330 623,330 623,360 105,360" fill="var(--ink)"/>
      <line class="guide" x1="20" y1="0" x2="125" y2="439"/>
      <text class="display" x="588" y="82" font-size="36" text-anchor="end">Project Details</text>
      <text class="display" x="588" y="124" font-size="36" text-anchor="end">Site Location</text>
    </svg>
  </section>

  <!-- Site location: lot -->
  <section class="page page--site-lot">
    <svg viewBox="0 0 623 439" preserveAspectRatio="none">
      <rect x="0" y="0" width="623" height="439" fill="url(#sheen)"/>
      <polygon points="0,112 45,112 100,330 0,330" fill="var(--ink)"/>
      <polygon points="55,143 623,143 623,330 100,330" fill="var(--map-grey)" role="img" aria-label="Greyed aerial photograph of neighbouring lots"/>
      <polygon points="365,155 397,160 362,316 331,311" fill="var(--foliage)" stroke="var(--lot-edge)" stroke-width="2" role="img" aria-label="Aerial view of the site lot outlined"/>
      <polygon points="100,330 623,330 623,360 105,360" fill="var(--ink)"/>
      <line class="guide" x1="20" y1="0" x2="125" y2="439"/>
      <text class="display" x="588" y="82" font-size="36" text-anchor="end">Project Details</text>
      <text class="display" x="588" y="124" font-size="36" text-anchor="end">Site Location</text>
    </svg>
  </section>
</div>
</body>
</html>
```